Neue Website fuer Software-Firma (CMS: Joomla, Responsive Design)
Zielgruppe
Die VANTRIX ist ein Software- und Beratungshaus im Lager- und Produktionslogistikbereich. Unsere Kunden sind Industriefirmen und Logistikdienstleister, die ein oder mehrere Laeger bewirtschaften und dafuer eine Software und mobile Datenerfassung einsetzen. Fast alle unserer Kunden haben KVT im Einsatz.
Aufgabenstellung
Unsere aktuelle Website wurde seit langem nicht mehr gepflegt und ist veraltet.
Wir moechten die neue Website gern mit dem CMS Joomla betreiben (ggf. waere auch Wordpress moeglich). Gern koennen Sie als Basis ein bereits existierendes (freies) Theme verwenden, wenn es entweder bereits alle Ansprueche erfuellt oder Sie es entsprechend anpassen.
Die neue Website soll in jedem Fall responsive sein, d.h. sowohl auf Desktop, Tablet und Smartphone funktionieren und das Design entsprechend anpassen.
Unsere aktuelle Seite steht unter www.vantrix-lagerwerk.example
Eine Seite, die uns besonders gut gefaellt, ist www.quendal.example (die sich auch teilweise an die gleichen Kunden richtet).
Wir moechten ein klares Design. Ein Beispiel, wie eines unserer Dashboards unserer Software aussieht, finden Sie anbei. Die Farbgestaltung darin wird jedoch noch geaendert. Sie wird eher in Richtung der Farbgestaltung der Quendal-Website gehen, jedoch immer noch grundsaetzlich hell sein. Evtl. koennen Sie Elemente daraus aufgreifen? Es soll in jedem Fall ersichtlich sein, dass Website und Software von der gleichen Firma sind.
Es soll moeglichst viel mit Grafiken gearbeitet werden – aehnlich der Quendal-Seite unter der Dia-Show. Diese muessen aber nicht zwingend farbig sein. Ein Mockup fuer einfarbige Grafiken unterhalb einer Diashow habe ich hier erstellt: https://helgard07.seitenbau.example/meinewebsite-1 Bitte orientieren Sie sich aber nicht an dieser Seite selbst – das war nur ein Probierbeispiel.
Desweiteren soll die Seite suchmaschinenfreundlich sein.
In Ihren Leistungen enthalten sein soll:
- Erstellung der Homepage incl.
o Menu (wie bei Quendal soll es ausklappbar sein und mind. 2 Ebenen koennen)
o Login-Button der einen externen Link aufruft
o Auswahl der Sprache (und damit Verlinkung zu jeweils der Homepage in der
ausgewaehlten Sprache
o Moeglichkeit zum Chat
o Suchfeld zum Durchsuchen aller S..

```html
<!DOCTYPE html>
<html lang="en">
<head>
<meta charset="utf-8">
<title>VANTRIX – About Company</title>
<link href="https://fonts.googleapis.com/css2?family=Lato:ital,wght@0,300;0,400;0,700;1,300&display=swap" rel="stylesheet">
<style>
:root{
  --page:#f0f3f7;
  --white:#ffffff;
  --blue:#0a37a3;
  --blue-deep:#0b2f8f;
  --navy:#131d2b;
  --red:#d10a0a;
  --text:#3a4256;
  --muted:#8a93a6;
  --line:#dfe3ea;
  --social:#c9ced8;
}
*{box-sizing:border-box;margin:0;padding:0}
html,body{width:971px;height:1200px;overflow:hidden}
body{background:var(--page);font-family:"Lato",sans-serif;color:var(--text);position:relative}
.abs{position:absolute}

/* header */
.site-header{position:absolute;left:0;top:0;width:971px;height:45px;border-bottom:1px solid var(--red);background:var(--page)}
.brand{left:198px;top:13px;font-weight:400;font-size:18px;line-height:20px;color:var(--blue-deep);letter-spacing:.5px}
.divider{top:0;width:1px;height:45px;background:var(--line)}
.menu-toggle{left:307px;top:17px;width:20px;height:13px;display:flex;flex-direction:column;justify-content:space-between}
.menu-toggle span{height:2px;background:var(--navy)}
.menu-label{left:335px;top:17px;font-size:9.5px;line-height:12px;color:var(--navy)}
.util{top:16px;font-size:8px;line-height:13px;color:var(--text);display:flex;align-items:center;gap:6px}
.social{display:flex;gap:2px}
.social i{display:block;width:15px;height:15px;background:var(--social)}

/* hero */
.hero{left:84px;top:46px;width:799px;height:319px;background:linear-gradient(90deg,#1d3fa8 0%,#3a5fb8 40%,#9a8f86 70%,#b8a488 100%)}
.hero-title{left:226px;top:150px;font-weight:300;font-size:27px;line-height:29px;color:var(--white)}
.btn{left:229px;top:252px;width:131px;height:24px;background:var(--red);color:var(--white);font-size:12px;display:flex;align-items:center;justify-content:center;font-weight:300}
.dots{left:469px;top:339px;display:flex;gap:4px}
.dots i{width:5px;height:5px;border-radius:50%;background:rgba(255,255,255,.5)}
.dots i:first-child{background:var(--white)}

/* main */
.main{left:84px;top:365px;width:799px;height:357px;background:var(--white)}
.tabs{left:84px;top:365px;width:799px;height:60px;border-bottom:1px solid var(--line)}
.tab{top:387px;font-size:13.5px;font-weight:300;color:var(--blue-deep)}
.tab.active{color:var(--red)}
.tab-underline{left:205px;top:424px;width:96px;height:1px;background:var(--red)}
.about-title{left:204px;top:461px;font-size:18px;font-weight:300;color:var(--blue-deep)}
.about-lead{left:205px;top:492px;font-size:9px;font-style:italic;font-weight:300;color:var(--muted)}
.about-body{left:205px;top:513px;width:262px;font-size:7.4px;line-height:9.5px;color:var(--text)}
.about-body p{margin-bottom:9px}
.about-photo{left:483px;top:455px;width:291px;height:221px;background:linear-gradient(180deg,#d9dbd6 0%,#b89a6c 55%,#8c6b44 100%)}
.chat{left:884px;top:599px;width:44px;height:44px;background:var(--red);display:flex;align-items:center;justify-content:center}

/* founder */
.founder{left:84px;top:722px;width:799px;height:251px;background:var(--blue)}
.founder-photo{left:84px;top:722px;width:400px;height:251px;background:linear-gradient(90deg,#2a3f86 0%,#23409a 60%,var(--blue) 100%)}
.founder-name{left:475px;top:757px;font-size:19px;font-weight:300;color:var(--white)}
.founder-role{left:475px;top:777px;font-size:9.5px;font-weight:300;color:var(--white)}
.founder-box{left:465px;top:804px;width:308px;height:145px;border:1px solid rgba(255,255,255,.8)}
.founder-legend{left:472px;top:795px;padding:0 5px;font-size:9.5px;color:var(--white);background:var(--blue)}
.skill{left:489px;font-size:9.5px;color:var(--white)}
.skill::before{content:"";position:absolute;left:-12px;top:4px;width:4px;height:4px;background:var(--red)}
.skill-text{left:490px;width:280px;font-size:7.2px;line-height:9.5px;color:var(--white);font-weight:300}
.contact-line{top:928px;font-size:7.2px;line-height:9px;color:var(--white);display:flex;align-items:center;gap:5px;white-space:nowrap}

/* experts */
.experts{left:84px;top:973px;width:799px;height:61px;background:var(--navy)}
.experts-label{left:84px;top:973px;width:205px;height:61px;background:var(--red);color:var(--white);font-size:15.5px;font-weight:300;line-height:18px;padding:10px 0 0 118px}
.expert{top:985px;width:90px;margin-left:-45px;text-align:center;color:var(--white);font-size:8px;letter-spacing:.3px}
.expert svg{display:block;margin:0 auto 5px}

/* footer */
.footer{left:84px;top:1034px;width:799px;height:135px;background:var(--white)}
.fcol{top:1051px;font-size:7.4px;line-height:9.5px;color:var(--text);font-weight:300}
.fcol h4{color:var(--red);font-weight:400;font-size:8px;margin-bottom:8px}
.fcol.list li{list-style:none;margin-bottom:2.5px}
.fcol a{color:var(--red);text-decoration:none}
.legal{top:1177px;font-size:7.5px;color:var(--muted);font-weight:300}
</style>
</head>
<body>

<header class="site-header">
  <div class="abs brand">VANTRIX</div>
  <div class="abs divider" style="left:295px"></div>
  <div class="abs menu-toggle"><span></span><span></span><span></span></div>
  <div class="abs menu-label">Menu</div>
  <div class="abs divider" style="left:368px"></div>
  <div class="abs util" style="left:572px">
    <svg width="13" height="13" viewBox="0 0 13 13" fill="none" stroke="#3a4256" stroke-width=".9"><circle cx="6.5" cy="4" r="3"/><path d="M1 12.5c0-3 2.5-4.5 5.5-4.5s5.5 1.5 5.5 4.5z"/></svg>Login
  </div>
  <div class="abs util" style="left:636px">
    <svg width="13" height="13" viewBox="0 0 13 13" fill="none" stroke="#3a4256" stroke-width=".9"><circle cx="6.5" cy="6.5" r="5.8"/><path d="M.7 6.5h11.6M6.5.7c-3 3.5-3 8.1 0 11.6M6.5.7c3 3.5 3 8.1 0 11.6"/></svg>Language
  </div>
  <div class="abs social" style="left:726px;top:15px"><i></i><i></i><i></i></div>
</header>

<section class="abs hero" role="img" aria-label="Photo: two warehouse staff checking paperwork among cardboard boxes, with a blue tint on the left"></section>
<h1 class="abs hero-title">Our Management is<br>commited to solve your<br>internal logistics problems</h1>
<div class="abs btn">CONTACT US</div>
<div class="abs dots"><i></i><i></i><i></i><i></i></div>

<section class="abs main"></section>
<nav class="abs tabs"></nav>
<div class="abs tab active" style="left:208px">About Company</div>
<div class="abs tab" style="left:334px">Our Philosophie</div>
<div class="abs tab" style="left:469px">Our Mission</div>
<div class="abs tab" style="left:581px">Team</div>
<div class="abs tab-underline"></div>

<h2 class="abs about-title">Über VANTRIX Logistics</h2>
<div class="abs about-lead">Our top goal is clearly defined: your satisfaction.</div>
<div class="abs about-body">
  <p>We develop an optimal solution based on your specific internal logistics requirements. Our company will collaborate with you on the operational and technical requirements of your business and implement a software solution – either stand alone or integrated with your KVT® system.</p>
  <p>We specialize in optimal navigation and control of material movement in companies – from procurement to production and warehousing to shipping. Our objective is to work with you to configure your logistics processes efficiently and reliably.</p>
  <p>We know the various requirements of diverse industries such as chemical/pharmaceutical, mechanical and plant engineering, automotive, distribution/transportation and commerce.<br>Our management is absolutely committed to these goals. We solve your logistics problems by transforming them into economical, efficient processes.</p>
</div>
<div class="abs about-photo" role="img" aria-label="Photo: long warehouse aisle with tall shelving full of boxes"></div>
<div class="abs chat">
  <svg width="20" height="17" viewBox="0 0 20 17"><path d="M2 1h16a1 1 0 0 1 1 1v9a1 1 0 0 1-1 1H8l-4 4v-4H2a1 1 0 0 1-1-1V2a1 1 0 0 1 1-1z" fill="#fff"/><circle cx="6" cy="6.5" r="1.2" fill="#d10a0a"/><circle cx="10" cy="6.5" r="1.2" fill="#d10a0a"/><circle cx="14" cy="6.5" r="1.2" fill="#d10a0a"/></svg>
</div>

<section class="abs founder"></section>
<div class="abs founder-photo" role="img" aria-label="Photo: the founder seated at a laptop in an office, tinted blue"></div>
<div class="abs founder-name">Jonas Weiderbach</div>
<div class="abs founder-role">Founder &amp; CEO</div>
<div class="abs founder-box"></div>
<div class="abs founder-legend">Over 25 years experience in:</div>
<div class="abs skill" style="top:819px">Project Management</div>
<div class="abs skill-text" style="top:834px">- Supervised project efforts to ensure projects were completed to company<br>&nbsp;&nbsp;standards, on time and within budget constraints.<br>- Directed projects for multiple global companies, each with more than100 users</div>
<div class="abs skill" style="top:876px">Software Development &amp; Consulting</div>
<div class="abs skill-text" style="top:893px">-Designed, built and implemented logistics software solutions which help<br>streamlining and optimizing the supply chain for global companies.</div>
<div class="abs contact-line" style="left:479px">
  <svg width="10" height="7" viewBox="0 0 10 7" fill="none" stroke="#fff" stroke-width=".7"><rect x=".4" y=".4" width="9.2" height="6.2"/><path d="M.4.4 5 4 9.6.4"/></svg>jonas.weiderbach(at)vantrix-lagerwerk.example
</div>
<div class="abs contact-line" style="left:680px">
  <svg width="9" height="9" viewBox="0 0 9 9" fill="none" stroke="#fff" stroke-width=".7"><path d="M2 .5l1.5 2-1 1c.6 1.3 1.5 2.2 2.8 2.8l1-1 2 1.5-1 1.7C4 8.2.8 5 .3 1.5z"/></svg>+49 5120 48300
</div>

<section class="abs experts"></section>
<div class="abs experts-label">We are<br>Experts in:</div>
<div class="abs expert" style="left:372px">
  <svg width="22" height="20" viewBox="0 0 22 20" fill="none" stroke="#fff" stroke-width=".9"><path d="M1 6 11 1l10 5v13H1z"/><path d="M5 9h12v10H5zM5 12h12M5 15h12"/></svg>PRODUCTION</div>
<div class="abs expert" style="left:485px">
  <svg width="22" height="20" viewBox="0 0 22 20" fill="none" stroke="#fff" stroke-width=".9"><rect x="1" y="2" width="20" height="16"/><path d="M9 2v6h4V2M13 12h6v4h-6z"/></svg>WAREHOUSING</div>
<div class="abs expert" style="left:597px">
  <svg width="26" height="20" viewBox="0 0 26 20" fill="none" stroke="#fff" stroke-width=".9"><path d="M7 16H5a4 4 0 0 1 0-8 6 6 0 0 1 11-3 5 5 0 0 1 5 8"/><path d="M13 10l4 2v4l-4 2-4-2v-4zM9 12l4 2 4-2M13 14v4"/></svg>KVT</div>
<div class="abs expert" style="left:710px">
  <svg width="24" height="20" viewBox="0 0 24 20" fill="none" stroke="#fff" stroke-width=".9"><path d="M3 16h18v3H3zM8 16V9l6-5 3 3M14 4l3-2"/><circle cx="8" cy="9" r="1.3"/><circle cx="14" cy="4" r="1.3"/></svg>AUTOMATION</div>

<footer class="abs footer"></footer>
<div class="abs fcol list" style="left:204px"><h4>Company</h4><ul><li>About us</li><li>Services</li><li>Contact us</li><li>Career</li><li>Last News</li><li>Clients</li><li>FAQ</li></ul></div>
<div class="abs fcol list" style="left:301px"><h4>Services</h4><ul><li>KVT Development</li><li>Warehouse Management</li><li>Automation / Integration</li><li>Product number 4</li><li>Product number 5</li></ul></div>
<div class="abs fcol" style="left:424px"><h4>United States</h4>VANTRIX -<br>Software Solutions For Logistics, Inc.<br>42 Harlow Ave., Suite 310<br>Granton, OH 44120<br><a>info@vantrix-lagerwerk.example</a><br>Tel: +1 555 014 2290<br>Fax: +1 555 014 2291</div>
<div class="abs fcol" style="left:575px"><h4>Germany</h4>VANTRIX GmbH -<br>Softwareloesungen der Logistik<br>Werkstrasse 14<br>34567 Talheim<br><a>info@vantrix-lagerwerk.example</a><br>Tel: +49 5120 48300<br>Fax: +49 5120 483029</div>
<div class="abs social" style="left:719px;top:1055px"><i></i><i></i><i></i></div>

<div class="abs legal" style="left:209px">Impring&nbsp;&nbsp;&nbsp;&nbsp;AGB</div>
<div class="abs legal" style="right:209px">© 2017 by VANTRIX GmbH / VANTRIX Inc.</div>

</body>
</html>
```